Celling poster

It is a celling poster with questions that you ask yourself in the morning and a morning prayer + evening questions. People might put it on celling or on the wall.

Here is the contant, it is in Slovenian, but I have send you translation.

PO JUTRU SE DAN POZNA ...

1. Kaj me trenutno najbolj veseli v življenju?
3. Na kaj sem ponosna v življenju?
4. Za katere stvari danes čutim največ hvaležnosti?
5. V čem trenutno najbolj uživam?
6. Koga imam rada in kdo me ima rad?

Danes vstajam
s pomočjo nebeških sil:
svetlobe sonca,
sija lune,
žara ognja,
hitrosti strele,
okretnosti vetra,
globine morja,
stanovitnosti zemlje,
trdnosti skale.

VEČERNE MODROSTI

1. Kaj je bil danes moj prispevek svetu?
2. Kaj sem se danes naučila?
3. Katera situacija v dnevu mi je prinesla največ občutkov topline?

TRANSLATION for your understanding.

MORNING POWER QUESTIONS
1. What am I happy abou in my life right now?
2. What am I excited about in my life now?
3. What am I proud about in my life now?
4. What am I grateful about in my life now?
5. What am I enjoying most in my life now?
6. Who do I love? Who loves me?

MORNING PRAYER
Today I am waking up with the power of heavenly forces.
With the light of sun,
light of moon,
light of fire,
speed of lightning,
flexibility of wind,
depps of ocean,
stability of earth and
hardness of rock.

EVENING QUESTIONS OF WISDOM
1. What have I given today?
2. What did I learn today?
3. Which situations today gave me the most feelings of love, warmth?

```html
<!DOCTYPE html>
<html lang="sl">
<head>
<meta charset="utf-8">
<title>Po jutru se dan pozna – stropni plakat</title>
<link rel="stylesheet" href="https://fonts.googleapis.com/css2?family=Arimo:ital,wght@1,700&family=Playfair+Display:ital,wght@1,700&display=swap">
<style>
  :root {
    --sky-top: #5f8f8c;
    --sky-mid: #c9b35a;
    --sky-gold: #f2c63a;
    --sun-core: #fffbe6;
    --sun-glow: #ffe27a;
    --hills: #3a2a12;
    --frame-line: #ffffff;
    --panel-light: rgba(255, 255, 255, 0.38);
    --panel-grey: rgba(220, 215, 205, 0.42);
    --ink: #141414;
    --title-ink: #f4f0e6;
    --title-shadow: rgba(60, 50, 30, 0.65);
  }
  * { margin: 0; padding: 0; box-sizing: border-box; }
  html, body { width: 900px; height: 1200px; overflow: hidden; }
  body { position: relative; background: var(--hills); }

  .poster { position: relative; width: 900px; height: 1200px; overflow: hidden; }

  .sunrise-sky {
    position: absolute; inset: 0;
    background:
      radial-gradient(circle at 190px 690px, var(--sun-core) 0, var(--sun-core) 60px, rgba(255,240,170,0.85) 130px, rgba(255,220,110,0) 380px),
      radial-gradient(ellipse 700px 500px at 200px 700px, rgba(255,226,122,0.55), rgba(255,226,122,0) 70%),
      linear-gradient(180deg, var(--sky-top) 0%, #8ea27a 18%, var(--sky-mid) 35%, var(--sky-gold) 55%, #e0a52a 72%, #8a5a1e 84%, var(--hills) 100%);
  }

  .frame {
    position: absolute;
    border: 2px solid var(--frame-line);
    border-radius: 28px;
    box-shadow: 0 0 0 5px rgba(255,255,255,0.15), 0 2px 6px rgba(0,0,0,0.25);
  }
  .frame::before {
    content: ""; position: absolute; inset: 6px;
    border: 1.5px solid var(--frame-line);
    border-radius: 22px;
  }
  .frame--morning { left: 92px; top: 110px; width: 380px; height: 240px; background: var(--panel-light); }
  .frame--prayer { left: 556px; top: 390px; width: 246px; height: 440px; background: var(--panel-light); border-radius: 14px; }
  .frame--prayer::before { border-radius: 10px; }
  .frame--evening { left: 128px; top: 870px; width: 336px; height: 200px; background: var(--panel-grey); }

  .section-title {
    font-family: "Playfair Display", serif;
    font-weight: 700; font-style: italic;
    font-size: 19px; letter-spacing: 0.5px;
    color: var(--title-ink);
    text-shadow: 0 0 2px var(--title-shadow), 1px 1px 1px var(--title-shadow);
    position: absolute; white-space: nowrap;
  }

  .question-list {
    position: absolute; list-style: none;
    font-family: "Arimo", sans-serif;
    font-weight: 700; font-style: italic;
    font-size: 16px; line-height: 21px;
    color: var(--ink);
  }
  .question-list li { padding-left: 19px; text-indent: -19px; }

  .morning-title { left: 140px; top: 131px; }
  .morning-list { left: 125px; top: 156px; width: 330px; }

  .prayer-title { left: 590px; top: 457px; }
  .prayer-text {
    position: absolute; left: 566px; top: 503px; width: 220px;
    font-family: "Arimo", sans-serif;
    font-weight: 700; font-style: italic;
    font-size: 16px; line-height: 21.2px;
    color: var(--ink); text-align: center;
  }
  .prayer-text .lead { display: block; margin-bottom: 0; }

  .evening-title { left: 178px; top: 887px; }
  .evening-list { left: 158px; top: 914px; width: 290px; }
</style>
</head>
<body>
<main class="poster">
  <div class="sunrise-sky" role="img" aria-label="Fotografija sončnega vzhoda z žarečim soncem nad temnimi hribi in zlatimi oblaki"></div>

  <section class="frame frame--morning" aria-hidden="true"></section>
  <h2 class="section-title morning-title">PO JUTRU SE DAN POZNA ...</h2>
  <ol class="question-list morning-list">
    <li>1. Kaj me trenutno najbolj veseli v življenju?</li>
    <li>3. Na kaj sem ponosna v življenju?</li>
    <li>4. Za katere stvari danes čutim največ hvaležnosti?</li>
    <li>5. V čem trenutno najbolj uživam?</li>
    <li>6. Koga imam rada in kdo me ima rad?</li>
  </ol>

  <section class="frame frame--prayer" aria-hidden="true"></section>
  <h2 class="section-title prayer-title">DANES VSTAJAM</h2>
  <p class="prayer-text">
    <span class="lead">s pomočjo nebeških sil:</span>
    svetlobe sonca,<br>
    sija lune,<br>
    žara ognja,<br>
    hitrosti strele,<br>
    okretnosti vetra,<br>
    globine morja,<br>
    stanovitnosti zemlje,<br>
    trdnosti skale.
  </p>

  <section class="frame frame--evening" aria-hidden="true"></section>
  <h2 class="section-title evening-title">VEČERNE MODROSTI</h2>
  <ol class="question-list evening-list">
    <li>1. Kaj je bil danes moj prispevek svetu?</li>
    <li>2. Kaj sem se danes naučila?</li>
    <li>3. Katera situacija v dnevu mi je prinesla največ občutkov topline?</li>
  </ol>
</main>
</body>
</html>
```